ZOR Clinic

We are a telemedicine based HIV treatment, prevention and hep c clinic looking to help make our online presence known.

Target Market(s)

Future patients. We want to this be informative and have stock images of all different types of people

Industry/Entity Type

Medical

Coding

Coded - Design and coding required

Requirements
Must have
• A Home Page, A page on PrEP, HIV treatment and Hep C. A box in the corner that says book now and a contact us page.

```html
<!DOCTYPE html>
<html lang="en">
<head>
<meta charset="utf-8">
<title>ZOR Clinic — HIV prevention, HIV treatment and hepatitis C care</title>
<link href="https://fonts.googleapis.com/css2?family=Alegreya+Sans:wght@500;700;800&family=Roboto:wght@400;500;700&display=swap" rel="stylesheet">
<style>
:root{
  --blue:#0057b8;
  --blue-deep:#0a3f95;
  --blue-bright:#0a8fd8;
  --green:#6cb23a;
  --green-light:#8cc63f;
  --ink:#1c1c1c;
  --text:#555;
  --field:#f4f4f4;
  --line:#e3e3e3;
  --white:#fff;
}
*{box-sizing:border-box;margin:0;padding:0}
html,body{width:1200px;height:5245px;overflow:hidden;background:var(--white)}
body{font-family:"Roboto",sans-serif;color:var(--ink);position:relative}
.abs{position:absolute}
.head-font{font-family:"Alegreya Sans",sans-serif}
.btn{position:absolute;display:flex;align-items:center;justify-content:center;gap:8px;border-radius:30px;background:linear-gradient(90deg,var(--green),var(--green-light));color:#fff;font:700 13px "Roboto",sans-serif;text-transform:uppercase;letter-spacing:.3px;box-shadow:0 3px 8px rgba(0,0,0,.12)}
.btn .dot{width:12px;height:12px;border-radius:50%;background:#fff;position:relative}
.btn .dot::after{content:"";position:absolute;left:4px;top:3px;border-left:5px solid var(--green);border-top:3px solid transparent;border-bottom:3px solid transparent}
.photo{position:absolute}
/* header */
.brand{position:absolute;display:flex;align-items:center;gap:10px;font:800 24px "Alegreya Sans",sans-serif;color:var(--blue)}
.brand .mark{width:34px;height:34px;border-radius:50%;background:var(--green)}
.call{position:absolute;left:712px;top:26px;display:flex;gap:10px;align-items:center}
.call .ic{width:36px;height:36px;border-radius:50%;background:var(--blue);display:flex;align-items:center;justify-content:center}
.call small{display:block;font-size:11px;color:#444}
.call b{font-size:17px;color:var(--ink)}
.nav{position:absolute;top:90px;left:580px;display:flex;gap:30px;font-size:13px;color:#222}
.nav .on{color:var(--blue)}
.hero-title{position:absolute;left:597px;top:188px;font:700 46px/1.15 "Alegreya Sans",sans-serif;color:var(--ink);width:520px}
.hero-title em{font-style:normal;color:var(--blue)}
.hero-text{position:absolute;left:600px;top:366px;width:440px;font-size:14.5px;line-height:1.8;color:#222}
/* about */
.eyebrow{font:700 15px "Roboto",sans-serif;color:var(--blue);text-transform:uppercase}
.h2{font:700 34px/1.3 "Alegreya Sans",sans-serif}
.p{font-size:13px;line-height:1.85;color:var(--text);text-align:justify}
.center-title{position:absolute;left:0;width:1200px;text-align:center;font:700 42px "Alegreya Sans",sans-serif;color:var(--ink)}
.center-title em{font-style:normal;color:var(--blue)}
/* service rows */
.svc-title{position:absolute;font:700 31px "Alegreya Sans",sans-serif;color:var(--ink)}
.svc-text{position:absolute;width:378px}
.svc-text .p{margin-bottom:16px}
.badge{position:absolute;width:90px;height:90px;border-radius:50%;background:var(--blue);border:5px solid #fff;box-shadow:0 4px 12px rgba(0,0,0,.2);display:flex;align-items:center;justify-content:center}
/* cta */
.cta{position:absolute;left:0;top:2616px;width:1200px;height:450px;background:linear-gradient(100deg,var(--blue-bright),var(--blue) 55%,var(--blue-deep));color:#fff;text-align:center}
.cta h2{font:700 41px/1.08 "Alegreya Sans",sans-serif;margin:50px auto 0;width:700px}
.cta p{font-size:13px;line-height:1.9;width:820px;margin:26px auto 0}
.cta .call-btn{position:absolute;left:477px;top:330px;width:244px;height:44px;border-radius:24px;background:#fff;display:flex;align-items:center;gap:12px;padding-left:6px;color:var(--blue);font:700 15px "Roboto",sans-serif}
.cta .call-btn span.ic{width:34px;height:34px;border-radius:50%;background:var(--green);display:flex;align-items:center;justify-content:center}
/* care */
.care-item{position:absolute;width:300px}
.care-item h3{font:700 14px "Roboto",sans-serif;margin-bottom:12px}
.care-item p{font-size:12px;line-height:1.6;color:var(--text)}
.care-item.r{text-align:right}
.ico{position:absolute;width:70px;height:70px;border-radius:50%;background:#fff;box-shadow:0 3px 10px rgba(0,0,0,.15);display:flex;align-items:center;justify-content:center}
.ico i{width:52px;height:52px;border-radius:50%;display:flex;align-items:center;justify-content:center}
/* reviews */
.reviews{position:absolute;left:0;top:3691px;width:1200px;height:448px;background:linear-gradient(90deg,#58b132,var(--green-light))}
.reviews h2{position:absolute;top:66px;width:1200px;text-align:center;font:700 42px "Alegreya Sans",sans-serif;color:#fff}
.card{position:absolute;top:159px;width:381px;height:214px;background:#fff;border-radius:28px;box-shadow:0 6px 14px rgba(0,0,0,.12)}
.avatar{position:absolute;top:52px;left:-45px;width:104px;height:104px;border-radius:50%;border:4px solid #fff;background:linear-gradient(160deg,#c7a18a,#5b4a43)}
.card .q{position:absolute;left:96px;top:20px;font:700 60px/1 "Alegreya Sans",sans-serif;color:var(--blue)}
.card p{position:absolute;left:96px;top:74px;width:250px;font-size:12px;line-height:1.8;color:var(--text)}
.card b{position:absolute;left:96px;top:152px;font-size:14px}
.card .stars{position:absolute;left:96px;top:170px;color:#f5a623;font-size:16px;letter-spacing:1px}
.arrow{position:absolute;top:3940px;color:#fff}
/* contact */
.field-label{position:absolute;font:700 14px "Roboto",sans-serif}
.field{position:absolute;background:var(--field);border:1px solid var(--line);font-size:11px;color:#999;padding:15px 18px}
/* footer */
.footer{position:absolute;left:0;top:4808px;width:1200px;height:437px}
.footer h4{position:absolute;font:700 14px "Roboto",sans-serif;color:#fff}
.footer ul{position:absolute;list-style:none;font-size:12px;line-height:24px;color:#e6eeff}
.social{position:absolute;width:28px;height:28px;border-radius:50%;border:1.5px solid #fff}
.fc{position:absolute;color:#fff;font-size:12px;line-height:18px}
.fc b{font-size:11px;display:block}
</style>
</head>
<body>

<!-- HERO -->
<section class="abs" style="left:0;top:0;width:1200px;height:690px;background:linear-gradient(180deg,#e4f1fa,#f7fbfe 70%,#fff)">
  <div class="brand" style="left:143px;top:38px"><span class="mark"></span>ZOR Clinic</div>
  <div class="call">
    <span class="ic"><svg width="18" height="18" viewBox="0 0 24 24"><path fill="#fff" d="M6.6 10.8a15 15 0 0 0 6.6 6.6l2.2-2.2c.3-.3.7-.4 1-.2 1.1.4 2.3.6 3.6.6.6 0 1 .4 1 1V20c0 .6-.4 1-1 1A17 17 0 0 1 3 4c0-.6.4-1 1-1h3.5c.6 0 1 .4 1 1 0 1.3.2 2.5.6 3.6.1.3 0 .7-.2 1z"/></svg></span>
    <div><small>Call Us Today</small><b>800-555-0142</b></div>
  </div>
  <div class="btn" style="left:923px;top:24px;width:130px;height:39px;text-transform:none;font-weight:500">Book Now</div>
  <nav class="nav"><span class="on">Home</span><span>About Us</span><span>PrEP</span><span>HIV Treatment</span><span>Hep C</span><span>Contact Us</span></nav>
  <div class="photo" role="img" aria-label="Smiling couple embracing, woman in a straw hat" style="left:0;top:120px;width:590px;height:560px;background:radial-gradient(ellipse at 50% 45%,#c9a58c 0%,#7fa8cf 45%,#d9e9f5 75%,transparent 76%)"></div>
  <h1 class="hero-title">HIV prevention, HIV treatment and <em>hepatitis C care from anywhere</em></h1>
  <p class="hero-text">ZOR Clinic connects you with clinicians who specialize in PrEP, HIV and hep C.</p>
  <div class="btn" style="left:601px;top:450px;width:250px;height:55px">Book your first visit <span class="dot"></span></div>
  <svg class="abs" style="left:0;top:580px" width="1200" height="110" viewBox="0 0 1200 110">
    <path d="M0 65 C300 120 600 40 900 30 C1030 25 1120 50 1200 80 L1200 110 L0 110Z" fill="#fff"/>
    <path d="M0 65 C300 120 600 40 900 30 C1030 25 1120 50 1200 80" fill="none" stroke="var(--blue)" stroke-width="9"/>
    <path d="M700 45 C900 18 1050 30 1200 70" fill="none" stroke="#9cc8ea" stroke-width="3"/>
  </svg>
</section>

<!-- ABOUT -->
<section>
  <p class="eyebrow abs" style="left:143px;top:766px">About Us</p>
  <h2 class="h2 abs" style="left:143px;top:792px;width:440px">ZOR Clinic</h2>
  <div class="abs" style="left:143px;top:900px;width:425px">
    <p class="p">We care for people of every gender, sexuality, race, immigration status and income level — including people living far from an HIV clinic, people who have had bad experiences with the healthcare system, and people who simply want care that stays private.</p>
    <p class="p" style="margin-top:18px">If you are uninsured, we help you apply for medication assistance and coverage programs. Everything happens by video, phone and mail — private, affirming and built around your life.</p>
  </div>
  <div class="btn" style="left:143px;top:1120px;width:147px;height:41px">Read More <span class="dot"></span></div>
  <div class="abs" role="img" aria-label="Large brand decoration" style="left:650px;top:760px;width:420px;height:380px;display:flex;align-items:center;justify-content:center;gap:16px">
    <span style="width:120px;height:120px;border-radius:50%;background:linear-gradient(135deg,var(--green-light),var(--blue))"></span>
    <span class="head-font" style="font-weight:800;font-size:48px;color:var(--blue)">ZOR Clinic</span>
  </div>
</section>

<h2 class="center-title" style="top:1262px">What <em>We Do</em></h2>

<!-- SERVICES -->
<section>
  <div class="photo" role="img" aria-label="Young man holding a PrEP pill" style="left:0;top:1369px;width:599px;height:405px;background:linear-gradient(120deg,#d9d2cc,#b79f8e 50%,#8c8a88)"></div>
  <div class="badge" style="left:554px;top:1526px"><svg width="44" height="44" viewBox="0 0 44 44" fill="none" stroke="#fff" stroke-width="2.5"><rect x="10" y="8" width="20" height="28" rx="3"/><path d="M14 16h12M14 22h8"/><circle cx="31" cy="31" r="6"/></svg></div>
  <h3 class="svc-title" style="left:687px;top:1412px">PrEP for HIV prevention</h3>
  <div class="svc-text" style="left:687px;top:1470px">
    <p class="p">PrEP stands for pre-exposure prophylaxis. It is a daily pill — or, for some people, a long-acting injection given every two months — that keeps HIV from establishing an infection in your body. PrEP does not treat HIV; it prevents it.</p>
    <p class="p">PrEP prevents HIV only. Condoms still protect against other sexually transmitted infections, and we screen for STIs at every follow-up.</p>
  </div>
  <div class="btn" style="left:691px;top:1679px;width:145px;height:40px">Read More <span class="dot"></span></div>

  <h3 class="svc-title" style="left:141px;top:1820px">HIV treatment and care</h3>
  <div class="svc-text" style="left:141px;top:1878px">
    <p class="p">Today's HIV treatment is usually one pill a day with few side effects. With treatment, most people reach an undetectable viral load within a few months — living a long, healthy life and unable to transmit HIV to partners.</p>
    <p class="p">Antiretroviral therapy (ART) stops HIV from making copies of itself. As the amount of virus in your blood falls, your immune system recovers.</p>
  </div>
  <div class="btn" style="left:145px;top:2087px;width:145px;height:40px">Read More <span class="dot"></span></div>
  <div class="photo" role="img" aria-label="Close-up of an arm with a skin rash" style="left:599px;top:1774px;width:601px;height:408px;background:linear-gradient(120deg,#eef0f1,#d9c2b5 55%,#c9a894)"></div>
  <div class="badge" style="left:554px;top:1930px"><svg width="44" height="44" viewBox="0 0 44 44" fill="none" stroke="#fff" stroke-width="2.5"><rect x="17" y="6" width="10" height="32" rx="5"/><path d="M17 24h10"/></svg></div>

  <div class="photo" role="img" aria-label="Woman holding her side with liver highlighted" style="left:0;top:2182px;width:599px;height:434px;background:linear-gradient(120deg,#e8ebee,#b4896f 50%,#e07a3c 70%,#d6cfc9)"></div>
  <div class="badge" style="left:554px;top:2338px"><svg width="44" height="44" viewBox="0 0 44 44" fill="none" stroke="#fff" stroke-width="2.5"><path d="M8 14c6-6 22-6 28 0 2 8-6 18-14 18S6 22 8 14z"/><circle cx="30" cy="30" r="6"/></svg></div>
  <h3 class="svc-title" style="left:687px;top:2240px">Hepatitis C testing and cure</h3>
  <div class="svc-text" style="left:687px;top:2300px">
    <p class="p">Modern direct-acting antiviral pills cure more than 95% of people with hepatitis C, with very few side effects. We test, treat and confirm your cure entirely by telehealth.</p>
    <p class="p">Hepatitis C often causes no symptoms for years while it quietly scars the liver. The national health agency recommends that every adult be tested at least once, and more often for people who inject drugs, are pregnant, are living with HIV, received a blood transfusion</p>
  </div>
  <div class="btn" style="left:691px;top:2510px;width:145px;height:40px">Read More <span class="dot"></span></div>
</section>

<!-- CTA -->
<section class="cta">
  <h2>Get tested, get treated, get cured. Book a hepatitis C visit today.</h2>
  <p>Sed ut perspiciatis unde omnis iste natus error sit voluptatem accusantium doloremque laudantium, totam rem aperiam, eaque ipsa quae ab illo inventore veritatis et quasi architecto beatae vitae dicta sunt explicabo.</p>
  <p style="margin-top:22px;line-height:1.7"><b style="font-size:14px">We are here for you!</b><br>Our care can make a difference in your healing!</p>
  <div class="call-btn"><span class="ic"><svg width="16" height="16" viewBox="0 0 24 24"><path fill="#fff" d="M6.6 10.8a15 15 0 0 0 6.6 6.6l2.2-2.2c.3-.3.7-.4 1-.2 1.1.4 2.3.6 3.6.6.6 0 1 .4 1 1V20c0 .6-.4 1-1 1A17 17 0 0 1 3 4c0-.6.4-1 1-1h3.5c.6 0 1 .4 1 1 0 1.3.2 2.5.6 3.6.1.3 0 .7-.2 1z"/></svg></span>CALL: (800) 555-0199</div>
</section>

<!-- CARE -->
<section>
  <h2 class="center-title" style="top:3136px"><em>What care</em> looks like</h2>
  <div class="ico" style="left:384px;top:3230px"><i style="background:var(--blue)"><svg width="26" height="26" viewBox="0 0 24 24" fill="none" stroke="#fff" stroke-width="2"><rect x="3" y="5" width="13" height="14" rx="2"/><path d="M16 10l5-3v10l-5-3"/></svg></i></div>
  <div class="care-item r" style="left:178px;top:3320px"><h3>Meet by video or phone</h3><p>Book a visit with a licensed clinician — no waiting rooms, no travel, evenings available.</p></div>
  <div class="ico" style="left:734px;top:3230px"><i style="background:var(--green)"><svg width="26" height="26" viewBox="0 0 24 24" fill="none" stroke="#fff" stroke-width="2"><rect x="5" y="8" width="14" height="13" rx="2"/><path d="M7 4h10v4H7z"/></svg></i></div>
  <div class="care-item" style="left:734px;top:3320px;width:330px"><h3>Medication delivered</h3><p>Confidential records, affirming care, and help navigating insurance or assistance programs.</p></div>
  <div class="ico" style="left:384px;top:3443px"><i style="background:var(--green)"><svg width="26" height="26" viewBox="0 0 24 24" fill="none" stroke="#fff" stroke-width="2"><rect x="3" y="4" width="18" height="13" rx="2"/><path d="M8 21h8M12 17v4"/></svg></i></div>
  <div class="care-item r" style="left:160px;top:3540px;width:318px"><h3>Labs on your schedule</h3><p>At-home collection kits or a nearby lab draw, with results reviewed by your care team.</p></div>
  <div class="ico" style="left:734px;top:3443px"><i style="background:var(--blue)"><svg width="26" height="26" viewBox="0 0 24 24" fill="none" stroke="#fff" stroke-width="2"><rect x="5" y="10" width="14" height="11" rx="2"/><path d="M8 10V7a4 4 0 0 1 8 0v3"/></svg></i></div>
  <div class="care-item" style="left:734px;top:3540px;width:330px"><h3>Private and judgment-free</h3><p>Prescriptions shipped in discreet packaging, or sent to the pharmacy you already use.</p></div>
  <div class="abs" style="left:497px;top:3318px;width:196px;height:196px;border-radius:50%;background:#fff;box-shadow:0 6px 20px rgba(0,0,0,.15);display:flex;align-items:center;justify-content:center">
    <div style="width:160px;height:160px;border-radius:50%;border:3px solid var(--blue);display:flex;align-items:center;justify-content:center" class="head-font"><span style="font-weight:800;font-size:28px;color:var(--blue)">ZOR Clinic</span></div>
  </div>
</section>

<!-- REVIEWS -->
<section class="reviews">
  <h2>Customer Reviews</h2>
  <div class="card" style="left:198px"><span class="avatar" role="img" aria-label="Portrait of reviewer"></span><span class="q">“</span><p>Lorem ipsum dolor sit amet, consectetur adipiscing elit, sed do eiusmod tempor labore et dolore magna aliqua.</p><b>Dana R</b><span class="stars">★★★★★</span></div>
  <div class="card" style="left:672px"><span class="avatar" role="img" aria-label="Portrait of reviewer" style="background:linear-gradient(160deg,#b98e78,#3b2a25)"></span><span class="q">“</span><p>Lorem ipsum dolor sit amet, consectetur adipiscing elit, sed do eiusmod tempor labore et dolore magna aliqua.</p><b>Lena M</b><span class="stars">★★★★★</span></div>
</section>
<svg class="arrow" style="left:76px" width="20" height="34" viewBox="0 0 20 34"><path d="M16 3L4 17l12 14" fill="none" stroke="#fff" stroke-width="4"/></svg>
<svg class="arrow" style="left:1100px" width="20" height="34" viewBox="0 0 20 34"><path d="M4 3l12 14L4 31" fill="none" stroke="#fff" stroke-width="4"/></svg>

<!-- CONTACT -->
<section>
  <h2 class="center-title" style="top:4212px">Contact <em>Us</em></h2>
  <span class="field-label" style="left:177px;top:4303px">Name:</span>
  <div class="field" style="left:177px;top:4329px;width:406px;height:43px">Enter Your Name</div>
  <span class="field-label" style="left:615px;top:4303px">Email:</span>
  <div class="field" style="left:615px;top:4329px;width:408px;height:43px">Enter Email Address</div>
  <span class="field-label" style="left:177px;top:4391px">Phone:</span>
  <div class="field" style="left:177px;top:4416px;width:406px;height:43px">Enter Phone Number</div>
  <span class="field-label" style="left:615px;top:4391px">Service</span>
  <div class="field" style="left:615px;top:4416px;width:408px;height:43px;display:flex;justify-content:space-between;padding-top:0;padding-bottom:0;align-items:center">Select Service<svg width="10" height="6"><path d="M0 0h10L5 6z" fill="#222"/></svg></div>
  <span class="field-label" style="left:177px;top:4478px">Message</span>
  <div class="field" style="left:177px;top:4502px;width:846px;height:83px">Enter Comments</div>
  <div class="btn" style="left:523px;top:4638px;width:153px;height:41px">Submit <span class="dot"></span></div>
</section>

<!-- FOOTER -->
<footer class="footer">
  <svg class="abs" style="left:0;top:0" width="1200" height="437" viewBox="0 0 1200 437">
    <defs><linearGradient id="fbg" x1="0" x2="1"><stop offset="0" stop-color="#0a8fd8"/><stop offset=".6" stop-color="#0057b8"/><stop offset="1" stop-color="#0a3f95"/></linearGradient></defs>
    <path d="M0 40 C250 100 500 90 760 40 C950 5 1100 15 1200 60 L1200 437 L0 437Z" fill="#6cb23a"/>
    <path d="M0 60 C250 130 520 110 780 60 C960 28 1100 40 1200 80 L1200 437 L0 437Z" fill="url(#fbg)"/>
  </svg>
  <div class="brand" style="left:153px;top:202px;color:#fff;font-size:22px"><span class="mark" style="width:26px;height:26px"></span>ZOR Clinic</div>
  <span class="social" style="left:165px;top:266px"></span><span class="social" style="left:203px;top:266px"></span><span class="social" style="left:240px;top:266px"></span><span class="social" style="left:278px;top:266px"></span>
  <h4 style="left:407px;top:155px">Quick Links</h4>
  <ul style="left:407px;top:190px"><li>Home</li><li>About Us</li><li>What We Do</li><li>Our Services</li><li>Doctors Network</li><li>Contact Us</li></ul>
  <h4 style="left:593px;top:155px">About Company</h4>
  <ul style="left:593px;top:190px"><li>Legal Information</li><li>Terms &amp; Condition</li><li>Privacy Policy</li><li>Support</li><li>Site Map</li><li>FAQ</li></ul>
  <h4 style="left:800px;top:155px">Contact Us</h4>
  <div class="fc" style="left:822px;top:195px"><b>Phone</b>(800) 555-0142</div>
  <div class="fc" style="left:822px;top:246px"><b>Email</b>hello@zorclinic.example</div>
  <div class="fc" style="left:822px;top:296px"><b>Location</b>418 Maple Row, Fairview,<br>IN 47000</div>
  <svg class="abs" style="left:798px;top:198px" width="12" height="12" viewBox="0 0 24 24"><path fill="#8cc63f" d="M6.6 10.8a15 15 0 0 0 6.6 6.6l2.2-2.2c.3-.3.7-.4 1-.2 1.1.4 2.3.6 3.6.6.6 0 1 .4 1 1V20c0 .6-.4 1-1 1A17 17 0 0 1 3 4c0-.6.4-1 1-1h3.5c.6 0 1 .4 1 1 0 1.3.2 2.5.6 3.6.1.3 0 .7-.2 1z"/></svg>
  <svg class="abs" style="left:797px;top:250px" width="14" height="11" viewBox="0 0 14 11"><rect width="14" height="11" fill="#8cc63f"/><path d="M0 0l7 6 7-6" fill="none" stroke="#0057b8"/></svg>
  <svg class="abs" style="left:799px;top:298px" width="11" height="15" viewBox="0 0 12 16"><path d="M6 0a6 6 0 0 0-6 6c0 4 6 10 6 10s6-6 6-10a6 6 0 0 0-6-6z" fill="#8cc63f"/><circle cx="6" cy="6" r="2" fill="#0057b8"/></svg>
  <div class="abs" style="left:143px;top:376px;width:914px;height:1px;background:rgba(255,255,255,.35)"></div>
  <span class="abs" style="left:1074px;top:356px;width:34px;height:34px;border-radius:50%;background:var(--green);display:flex;align-items:center;justify-content:center"><svg width="14" height="10"><path d="M1 9l6-7 6 7" fill="none" stroke="#fff" stroke-width="2.5"/></svg></span>
  <p class="abs" style="left:0;top:398px;width:1200px;text-align:center;font-size:12px;color:#e6eeff">2026 Copyright - ZOR Clinic. | All Rights Reserved</p>
</footer>

</body>
</html>
```